Dynamic Website Design For Dynamic Speaker and Business Coach!

Professional Website Design for a for a Professional Business coach, Business trainer, and Speaker.

Note: This is for design only. No coding required. We want to see your ideas for a great website! This will be a FUN design and not boring like others you may work on.

Please let your creative ideas flow. We have given you a ton of info along with videos to help you understand what we are after, however we WANT your creativity to shine through in your designs!

We are a professional company that has run hundreds of crowdsourced projects on multiple platforms. If you participate in this contest (we hope you do) you can expect great video feedback, consistent feedback, and also our guarantee that if we know your website design will not be what we are looking for we will notify you so you don’t waste your time if there is no chance of you winning.

We respect and recognize this is how you make your living and we will not play games. We look forward to an awesome contest and awesome website designs.

Design Brief:

We are looking for a fresh and fun new design for

http://www.brightpath-advisory.net

This individual (Dana Holloway) teaches and trains corporations and businesses in the fields of leadership, sales, communication, business operations etc. Additionally this business teaches and mentors business professionals in a small group level or 1 on 1.

The website needs to convey trust, professionalism, and affluent, while at the same time having some personality!

This business operates on 3 core principles that we would like to see incorporated into the logo if it is a good fit. The 3 principals are:

Focus
Accountability
Results

Here is a video to help explain what we like about the current site and what we don’t like:
http://clipvault.example/t/QwpLmr82kTnb

As you can see the website is geared towards business professionals. Please look over the website to learn what they do. Obviously this is not a good website so we need your help.

We want a website that is professional-looking, has personality and is geared more towards promoting Dana Holloway, the owner of Summit Path Advisory as a Speaker and Business Consultant. The more you can incorporate clean, professional and fun personality elements into the design, the better off you are at winning.

Here are some examples of other sites in their business that have some things we like:

http://velvetcompass.com Please watch video to learn what we like and don’t like:
http://clipvault.example/t/NrtHq7YpLwc

http://tallpinegrowth.com Please watch video to learn what we like and don’t like:
http://clipvault.example/t/J8vDkrWa

http://www.marthaquince.com Please watch video to learn what we like and don’t like:
http://clipvault.example/t/Pz3mx9Rb2Kq

http://www.vantix7.com Please watch video to learn what we like and don’t like:
http://clipvault.example/t/7Gwe4sNhydv

NOTE: We do not want to copy anything outright. We want to learn, model and take their ideas and make them better. We also want to be flexible and take what we like along with your creativity to make an amazing design.

Here is what we are looking for in more specific terms:

Colors: We like the darker blue (not the light blue like the site) and also a burnt orange. I’ve attached her Logo so you can get an idea and feel for the colors.

When looking at colors please know that the current site and look is NOT what we are going for. We are going for a clean and professional look but also a look that is BOLD, FUN, and Vibrant (hence the colors).

Menu: Horizontal. We like bold and easy to read menu items. Don’t make it small and cluttered.

Site Structure: Clean and easy to navigate. We have a lot of content to display so we need a clean structure that breaks up the text and content areas.
Images: Please pull images from the current site. We can always replace the images of course, but if you show them “their own stuff” in the new design you will be closer to winning because it will feel more like “them”

Look and Feel: Professional. Fun. High-End. Business-like. This website needs to convey that Dana Holloway and Summit Path Advisory are professional. That Dana Holloway is a sought-after Speaker and Business Consultant who knows what she is talking about; can be serious when she needs to be, but also likes to have fun with her clients. This site must convey that!

Content Areas: It is a safe bet that if it is on the current site we need it on the new site. So don’t drop anything as it makes it hard to “cut content”.

What we don't want: We do not want clutter, boring, or templates or themes. We don’t want too cartoony, too cute, or too fancy… Be creative!

Out of respect to professional designers who really are working hard to win if you do not follow this brief, you submit worn out themes, templates, or boring designs you will be eliminated. We are offering great prize money for this so we expect great visual designs.
Updates

Project Deadline Extended
Reason: Our client is out of town, and waiting to hear feedback from them. So, in the meantime, we wanted to keep the project going to see what else you designers can come up with. As soon as we hear back from our client, we will pass along the info. Thanks!

Target Market(s)

Target Audience is entrepreneurs and business professionals alike. This is all business to business stuff.

This person teaches and trains startups and billion dollar companies. The common thread is that they are all businesses and companies who need help in various areas including sales, communication, business operations, etc.

Industry/Entity Type

Business

Font styles to use
Sans Serif

Requirements
Must have
• Brief is very detailed. Please review
Nice to have
Should not have

```html
<!DOCTYPE html>
<html lang="en">
<head>
<meta charset="utf-8">
<title>Summit Path Advisory — Business Coaching</title>
<link href="https://fonts.googleapis.com/css2?family=Open+Sans:wght@300;400;600;700&family=Merienda:wght@400&display=swap" rel="stylesheet">
<style>
:root{
  --navy:#2a3589;
  --orange:#e2782b;
  --sky:#0a79c2;
  --ink:#333;
  --muted:#666;
  --panel:#f4f4f4;
  --line:#dcdcdc;
  --footer:#252324;
  --footer-bar:#3b3b3b;
  --white:#fff;
}
*{margin:0;padding:0;box-sizing:border-box}
html,body{width:818px;height:1200px;overflow:hidden;background:var(--white)}
body{position:relative;font-family:"Open Sans",Arial,sans-serif;color:var(--ink);font-size:9px}
.abs{position:absolute}
/* header */
.brand{left:74px;top:12px;display:flex;align-items:center;gap:8px}
.brand-dot{width:40px;height:40px;border-radius:50%;background:var(--orange)}
.brand-name{font-size:22px;font-weight:700;color:var(--navy);line-height:24px;white-space:nowrap}
.follow{right:72px;top:6px;display:flex;align-items:center;gap:4px;color:var(--orange);font-weight:700;font-size:10.5px}
.social-sq{width:15px;height:15px;border-radius:3px;background:var(--orange)}
.phone-top{right:72px;top:27px;color:var(--orange);font-weight:600;font-size:10.5px;display:flex;align-items:center;gap:6px}
.search{left:618px;top:46px;width:128px;height:24px;background:#efefef;border:1px solid #e2e2e2;color:#aaa;font-size:9px;padding:5px 6px}
.search svg{position:absolute;right:7px;top:6px}
/* nav */
.nav{left:0;top:77px;width:818px;height:36px;background:var(--navy);border-bottom:2px solid var(--orange)}
.nav-home{position:absolute;left:68px;top:0;width:34px;height:34px;background:var(--orange);display:flex;align-items:center;justify-content:center}
.nav ul{list-style:none;position:absolute;left:116px;top:0;display:flex;gap:22px;height:34px;align-items:center}
.nav li{color:var(--white);font-weight:700;font-size:10px}
/* hero */
.hero{left:0;top:113px;width:818px;height:274px;background:var(--sky)}
.video{left:70px;top:42px;width:350px;height:195px;border:2px solid var(--orange);background:linear-gradient(160deg,#3d82c4,#1d5e9e)}
.video-title{position:absolute;left:6px;top:16px;width:232px;font-family:Georgia,serif;color:var(--white);font-size:29px;line-height:32px;text-align:center;white-space:nowrap}
.video-bar{position:absolute;left:6px;bottom:6px;right:6px;height:22px;background:rgba(0,0,0,.45);border-radius:2px}
.video-bar .play{position:absolute;left:4px;top:3px;width:26px;height:16px}
.video-bar .track{position:absolute;left:42px;top:10px;right:50px;height:3px;background:#777}
.video-bar .hd{position:absolute;right:6px;top:5px;color:#ccc;font-size:8px;font-weight:700;font-style:italic}
.video-share{position:absolute;right:6px;top:6px;width:18px;height:18px;background:rgba(0,0,0,.5);border-radius:3px}
.tagline{left:448px;top:72px;width:290px;text-align:center;font-family:"Merienda",cursive;color:var(--white);font-size:17.5px;line-height:30px}
.btn{position:absolute;height:32px;background:var(--orange);color:var(--white);font-weight:700;font-size:15px;display:flex;align-items:center;justify-content:center;border-radius:3px;box-shadow:0 3px 4px rgba(0,0,0,.3)}
/* how we work */
.how-title{left:0;width:818px;top:403px;text-align:center;font-size:21px;font-weight:300;color:#333}
.how-rule{left:298px;top:438px;width:227px;height:1px;background:#999}
.how-accent{left:390px;top:436px;width:42px;height:4px;background:var(--orange)}
.card{position:absolute;top:476px;width:200px;height:109px;border:2px solid var(--navy);text-align:center}
.card.is-focus{border-color:var(--orange)}
.card-icon{position:absolute;left:78px;top:-24px;width:44px;height:44px;border-radius:50%;background:var(--navy);border:3px solid var(--white);display:flex;align-items:center;justify-content:center}
.card.is-focus .card-icon{box-shadow:0 0 0 2px var(--orange)}
.card h3{margin-top:26px;font-size:12px;font-weight:700;letter-spacing:.3px}
.card p{margin:8px auto 0;width:160px;font-size:8px;line-height:14.5px;color:var(--muted)}
/* content */
.box{position:absolute;top:613px;border:1px solid var(--line);background:var(--white)}
.box-head{height:36px;background:#f6f6f6;border-bottom:1px solid var(--line);font-size:16px;font-weight:700;padding:7px 7px;color:#111;white-space:nowrap}
.box-head span{color:var(--orange)}
.coach{left:68px;width:503px;height:249px}
.coach-body{padding:8px 7px;font-size:8.3px;line-height:15px}
.coach-body p{margin-bottom:14px}
.coach-body h4{color:var(--sky);font-weight:400;font-size:12.5px;margin:-3px 0 10px}
.checks{list-style:none}
.checks li{display:flex;align-items:center;gap:10px;line-height:15px;padding-left:4px}
.read-more{left:417px;top:218px;width:75px;height:25px;font-size:8.5px;font-weight:600;border-radius:2px;box-shadow:none}
.report{left:590px;width:159px;height:249px;text-align:center}
.report .box-head{font-size:13px;text-align:left;padding:9px 6px}
.report h5{margin-top:10px;font-size:11px;color:var(--orange);font-weight:600;line-height:15px}
.report h5 b{color:#111;display:block}
.report .signup{margin-top:12px;font-style:italic;font-weight:600;font-size:8.6px;color:#111}
.report .pitch{margin-top:10px;font-size:8.6px;line-height:15px;color:#111}
.report .pitch i{color:var(--orange)}
.field{margin:12px auto 0;width:137px;height:24px;background:#ececec;border:1px solid #ddd;text-align:left;padding:5px 7px;color:#999;font-size:8.5px}
.field+.field{margin-top:7px}
.send{left:92px;top:219px;width:55px;height:23px;font-size:10px;font-weight:600;border-radius:2px;box-shadow:none}
/* testimonial */
.quote-band{left:0;top:880px;width:818px;height:114px;background:var(--panel);border-top:1px solid #e5e5e5}
.quote-photo{left:81px;top:21px;width:99px;height:68px;border:1px solid #ddd;background:linear-gradient(180deg,#e9e5e1,#b59a85)}
.quote-text{left:197px;top:19px;width:545px;font-size:8.6px;line-height:14.5px}
.quote-by{left:197px;top:75px;font-size:8.6px}
.quote-by b{font-weight:700}
/* footer */
.footer{left:0;top:994px;width:818px;height:173px;background:var(--footer);color:var(--white)}
.f-brand{left:98px;top:12px;display:flex;align-items:center;gap:6px}
.f-brand .brand-dot{width:30px;height:30px}
.f-brand .brand-name{color:var(--orange);font-size:16px;line-height:18px}
.f-contact{left:73px;font-size:8.8px;display:flex;gap:6px;line-height:12px}
.f-res-title{left:308px;top:18px;font-size:12.5px}
.f-res-rule{left:308px;top:42px;width:221px;height:1px;background:#bbb}
.f-links{list-style:none;font-size:8.6px;line-height:17px}
.f-links li::before{content:"» ";color:#ccc}
.badges{left:592px;top:7px;width:150px;height:50px;background:var(--white);border:2px solid var(--orange);border-radius:3px;display:flex;align-items:center;justify-content:space-around}
.badge-round{width:36px;height:36px;border-radius:50%;background:#8a9bb0}
.badge-gold{width:36px;height:36px;border-radius:50%;background:#c8a34a}
.badge-sq{width:36px;height:34px;background:#d0602e}
.f-follow{left:592px;top:77px;width:150px;text-align:center;font-size:12px;font-weight:600}
.f-social{position:absolute;top:102px;width:38px;height:38px;background:var(--orange);border-radius:3px}
.f-bar{left:0;top:1167px;width:818px;height:33px;background:var(--footer-bar);color:var(--white);font-size:8.8px;text-align:center;line-height:33px}
</style>
</head>
<body>

<header>
  <div class="abs brand"><div class="brand-dot"></div><div class="brand-name">Summit Path<br>Advisory</div></div>
  <div class="abs follow">Follow Me :<span class="social-sq"></span><span class="social-sq"></span><span class="social-sq"></span></div>
  <div class="abs phone-top">
    <svg width="11" height="11" viewBox="0 0 12 12"><rect width="12" height="12" rx="2" fill="#e2782b"/><path d="M3.5 2.5l1.5 0 .6 2-1 .8c.5 1.1 1.2 1.8 2.2 2.3l.8-1 2 .6v1.5c-3.5.2-6.3-2.6-6.1-6.2z" fill="#fff"/></svg>
    (505) 555-0182
  </div>
  <div class="abs search">Search
    <svg width="10" height="10" viewBox="0 0 10 10"><circle cx="4" cy="4" r="3" stroke="#222" stroke-width="1.5" fill="none"/><path d="M6.3 6.3L9 9" stroke="#222" stroke-width="1.6"/></svg>
  </div>
</header>

<nav class="abs nav">
  <div class="nav-home"><svg width="16" height="14" viewBox="0 0 16 14"><path d="M8 0L0 7h2v7h4.5V9.5h3V14H14V7h2z" fill="#fff"/></svg></div>
  <ul>
    <li>Passion</li><li>Who We Are?</li><li>Speaker</li><li>Free Video</li><li>Web TV Show</li><li>Testimonials</li><li>Meridian Learning</li><li>Blog</li><li>Contact</li>
  </ul>
</nav>

<section class="abs hero">
  <div class="abs video" role="img" aria-label="Video still of the coach presenting on stage against a blue backdrop">
    <div class="video-title">Do You Need<br>More Focus,<br>Accountability<br>&amp; Results?</div>
    <div class="video-share"></div>
    <div class="video-bar">
      <svg class="play" viewBox="0 0 26 16"><rect width="26" height="16" fill="#111"/><path d="M10 4l7 4-7 4z" fill="#fff"/></svg>
      <div class="track"></div>
      <div class="hd">HD</div>
    </div>
  </div>
  <p class="abs tagline">We specialize in guiding leaders to become easier to follow. You’re in the Right Place.</p>
  <div class="btn" style="left:468px;top:205px;width:116px">Free Video</div>
  <div class="btn" style="left:598px;top:205px;width:116px">Web TV Show</div>
</section>

<h2 class="abs how-title">HOW WE WORK</h2>
<div class="abs how-rule"></div>
<div class="abs how-accent"></div>

<div class="card is-focus" style="left:84px">
  <div class="card-icon"><svg width="18" height="18" viewBox="0 0 18 18"><path d="M16 2L2 8l6 2 2 6z" fill="none" stroke="#fff" stroke-width="1.6" stroke-linejoin="round"/><path d="M8 10l8-8" stroke="#fff" stroke-width="1.4"/></svg></div>
  <h3>FOCUS</h3>
  <p>Morbi tristique, odio vitae elementum facilisis, nibh turpis blandit ipsum, vitae sagittis orci.</p>
</div>
<div class="card" style="left:311px">
  <div class="card-icon"><svg width="18" height="14" viewBox="0 0 18 14"><rect x="1" y="1" width="16" height="12" rx="1.5" fill="none" stroke="#fff" stroke-width="1.5"/><rect x="1" y="4" width="16" height="2" fill="#fff"/><rect x="3" y="9" width="5" height="1.5" fill="#fff"/></svg></div>
  <h3>ACCOUNTABILTY</h3>
  <p>Morbi tristique, odio vitae elementum facilisis, nibh turpis blandit ipsum, vitae sagittis orci.</p>
</div>
<div class="card" style="left:539px">
  <div class="card-icon"><svg width="16" height="16" viewBox="0 0 16 16"><path d="M2 7h3v8H2zM6 7l3-6c1.2 0 1.8.8 1.5 2L10 6h4c1 0 1.5 1 1.2 1.8L13.5 14c-.2.6-.7 1-1.3 1H6z" fill="none" stroke="#fff" stroke-width="1.4" stroke-linejoin="round"/></svg></div>
  <h3>RESULTS</h3>
  <p>Morbi tristique, odio vitae elementum facilisis, nibh turpis blandit ipsum, vitae sagittis orci.</p>
</div>

<section class="box coach">
  <div class="box-head"><span>ALBUQUERQUE BUSINESS</span> COACHING AND CONSULTING</div>
  <div class="coach-body">
    <p>Are you searching to bridge the gap between where you are and where you want to be?</p>
    <p>As you face greater pressure to “move the needle” on your company’s productivity and bottom line profitability, how prepared are you to step in and shine as the leader?</p>
    <h4>Albuquerque Business Coach: Focus, Accountability, &amp; Results</h4>
    <ul class="checks">
      <li><svg width="9" height="9" viewBox="0 0 9 9"><rect x=".6" y="1.6" width="6.8" height="6.8" fill="none" stroke="#333" stroke-width="1.1"/><path d="M2 4.5l2 2L8.5.8" fill="none" stroke="#333" stroke-width="1.4"/></svg>Development Of An Operational Plan That Links All Departments</li>
      <li><svg width="9" height="9" viewBox="0 0 9 9"><rect x=".6" y="1.6" width="6.8" height="6.8" fill="none" stroke="#333" stroke-width="1.1"/><path d="M2 4.5l2 2L8.5.8" fill="none" stroke="#333" stroke-width="1.4"/></svg>Implementation And Monitoring Individual And Departmental Plans</li>
      <li><svg width="9" height="9" viewBox="0 0 9 9"><rect x=".6" y="1.6" width="6.8" height="6.8" fill="none" stroke="#333" stroke-width="1.1"/><path d="M2 4.5l2 2L8.5.8" fill="none" stroke="#333" stroke-width="1.4"/></svg>Diagnosing Employee Training Needs</li>
      <li><svg width="9" height="9" viewBox="0 0 9 9"><rect x=".6" y="1.6" width="6.8" height="6.8" fill="none" stroke="#333" stroke-width="1.1"/><path d="M2 4.5l2 2L8.5.8" fill="none" stroke="#333" stroke-width="1.4"/></svg>Delivering The Training To Develop Leaders And Staff</li>
      <li><svg width="9" height="9" viewBox="0 0 9 9"><rect x=".6" y="1.6" width="6.8" height="6.8" fill="none" stroke="#333" stroke-width="1.1"/><path d="M2 4.5l2 2L8.5.8" fill="none" stroke="#333" stroke-width="1.4"/></svg>Coach Leaders, Individuals And Teams</li>
    </ul>
  </div>
  <div class="btn read-more">Read More</div>
</section>

<aside class="box report">
  <div class="box-head"><span>FREE REPORT</span> FORM</div>
  <h5>Change your thinking,<b>Change your results!</b></h5>
  <p class="signup">Sign up for my FREE report</p>
  <p class="pitch"><i>"Have Fun While Making Sales"</i> and make more money this month!</p>
  <div class="field">Name</div>
  <div class="field">Email</div>
  <div class="btn send">Send</div>
</aside>

<section class="abs quote-band">
  <div class="abs quote-photo" role="img" aria-label="Portrait photo of the reviewer"></div>
  <p class="abs quote-text">"Dana is an enthusiastic and engaging instructor who strives at every opportunity to provide a worthwhile and purposeful workshop to her audience. She is fun, easy to work with, and full of great information! A real asset to any organization looking for professional training."</p>
  <p class="abs quote-by"><b>Renee Calder</b> - Former Advanced Sales Training Manager</p>
</section>

<footer class="abs footer">
  <div class="abs f-brand"><div class="brand-dot"></div><div class="brand-name">Summit Path<br>Advisory</div></div>
  <div class="abs f-contact" style="top:76px"><svg width="7" height="10" viewBox="0 0 7 10"><path d="M3.5 0A3.5 3.5 0 0 0 0 3.5C0 6 3.5 10 3.5 10S7 6 7 3.5A3.5 3.5 0 0 0 3.5 0z" fill="#fff"/><circle cx="3.5" cy="3.5" r="1.2" fill="#252324"/></svg><span>4410 Larkspur Ave NE, #212, Albuquerque,<br>New Mexico, 87110</span></div>
  <div class="abs f-contact" style="top:112px"><svg width="9" height="9" viewBox="0 0 12 12"><path d="M1.5 .5l2.5 0 1 3-1.5 1.2c.8 1.6 1.8 2.6 3.3 3.4l1.2-1.5 3 1v2.5C5.5 10.4.6 5.5 1.5.5z" fill="#fff"/></svg>(505) 555-0182</div>
  <div class="abs f-contact" style="top:135px"><svg width="10" height="8" viewBox="0 0 10 8"><rect width="10" height="8" rx="1" fill="#fff"/><path d="M0 .5l5 4 5-4" stroke="#252324" fill="none"/></svg>dana@summitpathadvisory.net</div>

  <div class="abs f-res-title">Resources</div>
  <div class="abs f-res-rule"></div>
  <ul class="abs f-links" style="left:315px;top:56px"><li>Home</li><li>Passion</li><li>Who We Are?</li><li>Speaker</li><li>Free Video</li></ul>
  <ul class="abs f-links" style="left:441px;top:57px"><li>Web TV Show</li><li>Testimonial</li><li>Meridian Learning</li><li>Blog</li><li>Contact Us</li></ul>

  <div class="abs badges"><div class="badge-round"></div><div class="badge-gold"></div><div class="badge-sq"></div></div>
  <div class="abs f-follow">Follow Us :</div>
  <div class="f-social" style="left:606px"></div>
  <div class="f-social" style="left:650px"></div>
  <div class="f-social" style="left:694px"></div>
</footer>
<div class="abs f-bar">©2014 Summit Path Advisory</div>

</body>
</html>
```